Fiscal Sponsorship Program Flyer

We are seeking a designer to create a 1-2 flyer that explains our fiscal sponsorship program. This flyer will be used to recruit new projects that might be interested in utilizing our fiscal sponsorship services. The pertinent information about our program can be found in the attached PDF. For users who cannot access the PDF, please try this link: https://files.plovarimedia.net/deck/7QtR2wzoLkVa9pXcJ4nEuYhsT3bGdMf8eKqW5rZxN1yo/view?mode=public

Target Market(s)

New charitable projects that do not yet have their own 501(c)(3) status, and are seeking a fiscal sponsor.

Industry/Entity Type

Nonprofit/Charity

Requirements
Must have
• The flyer must include the language and detail included on the attached PDF. The desire is to reformat this to be more appealing and easy to read.

```html
<!DOCTYPE html>
<html lang="en">
<head>
<meta charset="utf-8">
<title>Brightwell Foundation – Fiscal Sponsorship Program</title>
<link rel="stylesheet" href="https://fonts.googleapis.com/css2?family=Playfair+Display:ital,wght@0,400;0,700;1,400&family=Mulish:wght@400;600&display=swap">
<style>
:root{
  --coral:#f15f64;
  --coral-soft:#fde3e1;
  --ink:#1c2a2f;
  --text:#2b3236;
  --stage:#efeff1;
  --panel:#f3f3f5;
  --white:#ffffff;
}
*{box-sizing:border-box;margin:0;padding:0}
html,body{width:1200px;height:798px;overflow:hidden;background:var(--stage)}
body{position:relative;font-family:"Playfair Display",Georgia,serif;color:var(--text)}
.page{position:absolute;top:58px;width:526px;height:681px;background:var(--white);overflow:hidden}
.page--front{left:55px;background:linear-gradient(90deg,#fff 0%,#f6f6f7 100%)}
.page--back{left:617px}
.abs{position:absolute}
.serif{font-family:"Playfair Display",Georgia,serif}
.sans{font-family:"Mulish",Arial,sans-serif}

/* front */
.brand-title{left:25px;top:26px;font-size:36px;line-height:36px;font-weight:700;color:var(--ink)}
.program-band{left:0;top:120px;width:526px;height:51px;background:var(--coral);border-bottom-right-radius:26px;color:#fff;font-size:22px;font-weight:700;padding:10px 0 0 25px}
.band-glow{left:0;top:171px;width:526px;height:90px;background:linear-gradient(180deg,var(--coral-soft),rgba(253,227,225,0))}
.section-heading{font-size:15px;font-weight:700;color:var(--coral);line-height:1.2}
.body-copy{font-size:9.6px;line-height:13.8px;color:var(--text)}
.body-copy p+p{margin-top:13px}
.mission{left:25px;top:192px;width:240px}
.mission .section-heading{margin-bottom:9px}
.what-is{left:25px;top:349px;width:242px}
.what-is .section-heading{margin-bottom:9px}
.eligibility-q{font-weight:700;color:var(--ink);margin-top:11px}
.criteria{list-style:none;margin-top:2px}
.criteria li{position:relative;padding-left:12px}
.criteria li span{position:absolute;left:0;color:var(--coral);font-size:8px}
.photo{left:281px;top:202px;width:223px;height:198px;border-top-left-radius:66px;background:radial-gradient(circle at 55% 35%,#bfe0ec 0%,#d9e6ea 30%,#c8b9a7 60%,#9b8470 100%);border-bottom:4px solid var(--coral)}
.philosophy{left:281px;top:400px;width:223px;height:246px;background:linear-gradient(180deg,#f1f2f3 0%,#fff 45%)}
.philosophy .section-heading{position:absolute;left:19px;top:16px}
.philosophy-quote{position:absolute;left:20px;top:50px;width:190px;border-left:1px solid var(--ink);padding-left:10px}
.philosophy-text{position:absolute;left:19px;top:126px;width:192px}
.footer{left:0;top:646px;width:526px;height:35px;background:var(--coral);color:#fff;font-size:9.5px}
.footer-item{position:absolute;top:11px;display:flex;align-items:center;gap:5px}
.footer-item svg{width:8px;height:8px}

/* back */
.values-panel{left:0;top:0;width:254px;height:346px;background:var(--panel);border-top-right-radius:60px}
.commit-glow{left:254px;top:0;width:272px;height:346px;background:linear-gradient(180deg,#fdf0ef 0%,#fff 60%)}
.values{left:30px;top:20px;width:200px}
.values .section-heading{margin-bottom:12px}
.value{margin-bottom:10px}
.value h3{font-size:10px;font-weight:700;color:var(--coral);margin-bottom:3px}
.value p{font-size:9.2px;line-height:12px}
.value p.sans{font-size:9px}
.commitments{left:282px;top:20px;width:225px}
.commitments .section-heading{margin-bottom:12px}
.commit{display:flex;gap:10px;margin-bottom:12px;font-size:9.6px;line-height:12px}
.commit svg{flex:0 0 20px;width:20px;height:20px;stroke:var(--coral);fill:none;stroke-width:1.2}
.commit .sans{font-size:9.4px}
.fee-band{left:0;top:346px;width:526px;height:38px;background:var(--coral);border-top-right-radius:34px;color:#fff;font-size:20px;font-weight:700;text-align:center;padding-top:6px}
.fee-glow{left:0;top:384px;width:526px;height:80px;background:linear-gradient(180deg,var(--coral-soft),rgba(253,227,225,0))}
.tier-divider{top:398px;width:1px;height:240px;background:#e2e2e4}
.tier{top:398px;width:171px}
.tier-head{text-align:center}
.tier-name{font-size:20px;font-weight:700;color:var(--ink);line-height:24px}
.tier-fee{font-size:10px;line-height:12px}
.tier-kind{font-size:12.5px;font-style:italic;color:var(--coral);margin-top:9px}
.tier-list{list-style:none;margin-top:9px;font-size:9.6px;line-height:13px}
.tier-list li{position:relative;padding-left:12px;margin-bottom:7.5px}
.tier-list li::before{content:"";position:absolute;left:1px;top:3px;width:6px;height:3px;border-left:1.2px solid var(--coral);border-bottom:1.2px solid var(--coral);transform:rotate(-45deg)}
.tier-note{font-size:9.6px;line-height:13.5px}
</style>
</head>
<body>

<section class="page page--front">
  <h1 class="abs brand-title">Brightwell<br>Foundation</h1>
  <div class="abs program-band">Fiscal Sponsorship Program</div>
  <div class="abs band-glow"></div>

  <div class="abs mission body-copy">
    <h2 class="section-heading">Mission &amp; Vision</h2>
    <p>The Brightwell Foundation, founded in 2010, exists to support social impact campaigns and organizations through educational, public engagement, and awareness efforts.</p>
    <p>Its vision is to strengthen the capacity of the social impact sector and its leaders by providing top-tier fiscal sponsorship services.</p>
  </div>

  <div class="abs what-is body-copy">
    <h2 class="section-heading">What is Fiscal Sponsorship?</h2>
    <p>Fiscal sponsorship refers to the practice of non-profit organizations offering their legal and tax-exempt status to charitable projects or groups engaged in activities related to the sponsoring organization's mission. Fiscal sponsors provide oversight, financial management, and other administrative services to build the capacity of charitable projects.</p>
    <p class="eligibility-q">What kinds of projects are eligible for fiscal sponsorship?</p>
    <p style="margin-top:2px">Brightwell Foundation uses the following broad criteria to determine whether or not a project is eligible for fiscal sponsorship:</p>
    <ol class="criteria">
      <li><span>1.</span>Mission alignment with the Brightwell Foundation;</li>
      <li><span>2.</span>Whether or not the project provides an educational, social or charitable benefit; and</li>
      <li><span>3.</span>Whether or not the project’s activities follow the IRS regulations governing 501(c)(3) public charities.</li>
    </ol>
  </div>

  <div class="abs photo" role="img" aria-label="Photo of two people bumping fists in front of a glowing globe"></div>

  <div class="abs philosophy body-copy">
    <h2 class="section-heading">Program Philosophy</h2>
    <p class="philosophy-quote">We believe we can accelerate the pace and scale of social change by providing strategic back office support to emerging projects, leaders and ideas.</p>
    <p class="philosophy-text">By providing light touch administrative and capacity building services, our fiscal sponsorship program takes the administrative burden off the shoulders of leaders and their projects to allow them to focus on what they do best - achieving impact and changing the world.</p>
  </div>

  <footer class="abs footer">
    <span class="footer-item" style="left:25px"><svg viewBox="0 0 10 10" fill="none" stroke="#fff" stroke-width="0.9"><circle cx="5" cy="5" r="4.3"/><ellipse cx="5" cy="5" rx="2" ry="4.3"/><path d="M0.7 5h8.6"/></svg>brightwellfoundation.org</span>
    <span class="footer-item" style="left:301px"><svg viewBox="0 0 10 8"><rect width="10" height="8" rx="1" fill="#fff"/><path d="M0.5 1l4.5 3.5L9.5 1" fill="none" stroke="var(--coral)" stroke-width="0.9"/></svg>info@brightwellfoundation.org</span>
  </footer>
</section>

<section class="page page--back">
  <div class="abs values-panel"></div>
  <div class="abs commit-glow"></div>

  <div class="abs values">
    <h2 class="section-heading">Organizational Values</h2>
    <div class="value"><h3>Trust</h3><p class="sans">We believe that all successful partnerships begin with a foundation of trust.</p></div>
    <div class="value"><h3>Relationships</h3><p>Our partners are central to our work. We honor our relationships through respect, communication and transparency.</p></div>
    <div class="value"><h3>Embrace Complexity &amp; Risk</h3><p>We understand that bold solutions to intractable social issues often require both complexity and risk.</p></div>
    <div class="value"><h3>Innovation</h3><p>We embrace continuous improvement, bold creativity and change.</p></div>
    <div class="value"><h3>Diversity</h3><p>We believe that all voices matter and that effective solutions are created when decision-making is inclusive across social, cultural and economic backgrounds.</p></div>
  </div>

  <div class="abs commitments">
    <h2 class="section-heading">Program Commitments</h2>
    <div class="commit"><svg viewBox="0 0 20 20"><path d="M2 10l16-7-5 14-4-5z M9 12l9-9"/></svg><p>Fast, simple and efficient fiscal sponsorship program</p></div>
    <div class="commit"><svg viewBox="0 0 20 20"><path d="M5 2h7l4 4v12H5z M12 2v4h4"/><circle cx="10.5" cy="11" r="3"/><path d="M9 11l1.2 1.2L12 10"/></svg><p>Free and fast approval process - our application can be completed in 30 minutes or less. There is no fee to apply, and most projects can expect to receive a response on their application within 2 weeks</p></div>
    <div class="commit"><svg viewBox="0 0 20 20"><circle cx="10" cy="10" r="7.5"/><ellipse cx="10" cy="10" rx="3.5" ry="7.5"/><path d="M2.5 10h15 M4 6h12 M4 14h8 M12 15l2 2 4-4"/></svg><p>No fees and no minimums; projects of any size are welcome to apply</p></div>
    <div class="commit"><svg viewBox="0 0 20 20"><circle cx="9" cy="9" r="7"/><ellipse cx="9" cy="9" rx="3" ry="7"/><path d="M2 9h14"/><circle cx="15" cy="15" r="2.5"/></svg><p class="sans">Easy onboarding process</p></div>
    <div class="commit"><svg viewBox="0 0 20 20"><circle cx="11" cy="5" r="2.2"/><path d="M7.5 11a3.5 3.5 0 0 1 7 0 M1 13l5-1 5 2 6-3 M1 17h10l7-4"/></svg><p>Dedicated customer service and customization of services, tailored to the individual sponsored project’s needs</p></div>
    <div class="commit"><svg viewBox="0 0 20 20"><circle cx="10" cy="10" r="2.5"/><circle cx="3" cy="4" r="1.3"/><circle cx="17" cy="4" r="1.3"/><circle cx="3" cy="16" r="1.3"/><circle cx="17" cy="16" r="1.3"/><circle cx="10" cy="2" r="1.1"/><path d="M4 5l4 3.5 M16 5l-4 3.5 M4 15l4-3.5 M16 15l-4-3.5 M10 3v4.5"/></svg><p>Complex, hybrid structures, partnerships and coalitions are strongly encouraged to apply</p></div>
  </div>

  <div class="abs fee-band">Fee Structure</div>
  <div class="abs fee-glow"></div>
  <div class="abs tier-divider" style="left:171px"></div>
  <div class="abs tier-divider" style="left:347px"></div>

  <div class="abs tier" style="left:0">
    <div class="tier-head"><div class="tier-name">Basic</div><div class="tier-fee">Fee: 4%</div><div class="tier-kind">Limited</div></div>
    <ul class="tier-list" style="padding-left:13px">
      <li>Project Fund Set-Up</li>
      <li>Administration &amp; Management</li>
      <li>Financial Management</li>
      <li>Grant Proposal Review</li>
      <li>Grant Contract Review</li>
      <li>Project Reporting</li>
      <li>Insurance</li>
      <li>Annual Audit and Form 990</li>
    </ul>
  </div>

  <div class="abs tier" style="left:175px">
    <div class="tier-head"><div class="tier-name">Standard</div><div class="tier-fee">Fee: 6%</div><div class="tier-kind">Comprehensive</div></div>
    <p class="tier-note" style="padding-left:5px;margin-top:11px">Basic Services +</p>
    <ul class="tier-list" style="padding-left:5px;margin-top:6px">
      <li>Customized Financial Reporting</li>
      <li>Monthly Financial Statements</li>
      <li>Subgranting/regranting to U.S.-based organizations</li>
      <li>Management of Vendor &amp; Independent Contractors (1099s)</li>
    </ul>
  </div>

  <div class="abs tier" style="left:350px">
    <div class="tier-head"><div class="tier-name">Premium</div><div class="tier-fee">Fee: 10% +</div><div class="tier-kind">Custom</div></div>
    <p class="tier-note" style="padding-left:7px;margin-top:10px">Standard Services + Custom Services tailored to individual project needs.</p>
    <p class="tier-note" style="padding-left:7px;margin-top:6px">Customization Options:</p>
    <ul class="tier-list" style="padding-left:7px;margin-top:2px">
      <li>Subgranting/regranting to international organizations</li>
      <li>Lobbying Filings</li>
      <li>Project Audit</li>
      <li>Grant Writing Assistance</li>
      <li>One-on-One Coaching</li>
    </ul>
  </div>

  <footer class="abs footer">
    <span class="footer-item" style="left:25px"><svg viewBox="0 0 10 10" fill="none" stroke="#fff" stroke-width="0.9"><circle cx="5" cy="5" r="4.3"/><ellipse cx="5" cy="5" rx="2" ry="4.3"/><path d="M0.7 5h8.6"/></svg>brightwellfoundation.org</span>
    <span class="footer-item" style="left:301px"><svg viewBox="0 0 10 8"><rect width="10" height="8" rx="1" fill="#fff"/><path d="M0.5 1l4.5 3.5L9.5 1" fill="none" stroke="var(--coral)" stroke-width="0.9"/></svg>info@brightwellfoundation.org</span>
  </footer>
</section>

</body>
</html>
```